Seeking a new website design for electrical contracting company

Pelham & Tracy electrical contracting needs a new website for pelham-tracy.com

We are looking for modern and something real cool with motion for a landing page. we have some cool images from our photo shoot. maybe even 3d motion our existing logo. we would like something we can edit with news and events and update a past project page. Also allow to take payment
stock images at
https://mirabelwhitfordphotography.pixfolio-example.com/Pelham-and-Tracy

Target Market(s)

construction , home owners , business owners,

Industry/Entity Type

construction , electrical

Coding

Coded - Design and coding required

Number of Pages Required

5+ page

Font styles to use
Serif
Sans Serif

Colors
0054AA
0677BA
7BADD7
CADEEF
E8F1F8
0094D4
00A9DD
6FCCEA
C7EBF8
E9F6FB
FFF300
FFF600
FEFA6F
FFFEC7
FFFEE8

Requirements
Must have
• excitement, motion, selling professionalism,

```html
<!DOCTYPE html>
<html lang="en">
<head>
<meta charset="utf-8">
<title>Pelham &amp; Tracy – Electrical Contracting</title>
<link href="https://fonts.googleapis.com/css2?family=Poppins:wght@400;500;600;700&display=swap" rel="stylesheet">
<style>
:root{
  --blue:#0054AA; --blue-2:#0677BA; --sky:#0094D4; --pale:#E8F1F8; --pale-2:#CADEEF;
  --ink:#0b0d12; --navy:#071a36; --text:#222; --muted:#6b7280; --white:#fff; --star:#f5b301;
}
*{box-sizing:border-box;margin:0;padding:0}
html,body{width:1200px;height:4204px;overflow:hidden}
body{font-family:'Poppins',sans-serif;color:var(--text);background:var(--white);position:relative}
.abs{position:absolute}
.img{position:absolute;border-radius:4px}
.btn{display:inline-block;background:var(--blue);color:#fff;font-size:13px;font-weight:500;padding:10px 24px;border-radius:20px}
.title{font-size:34px;font-weight:600;display:flex;align-items:center;gap:10px}
.title::before{content:"";width:6px;height:28px;background:var(--blue);transform:skewX(-18deg)}
.on-blue .title::before,.title.light::before{background:#fff}
.para{font-size:13px;line-height:1.6;color:var(--muted)}
.logo{display:flex;align-items:center;gap:10px;font-weight:700;font-size:20px;color:var(--blue)}
.logo .mark{width:36px;height:36px;background:var(--blue);border-radius:4px}
.arrows{display:flex;gap:8px}
.arrows span{width:30px;height:30px;border-radius:4px;display:flex;align-items:center;justify-content:center;background:var(--pale-2)}
.arrows span.active{background:var(--blue)}
.section{position:absolute;left:0;width:1200px}

/* nav */
.nav{top:0;height:112px;display:flex;align-items:center;padding:0 72px;justify-content:space-between}
.nav ul{display:flex;gap:28px;list-style:none;font-size:14px;font-weight:500;margin-left:auto;margin-right:28px}
.nav .phone{background:var(--blue);color:#fff;font-size:14px;font-weight:600;padding:9px 18px;border-radius:4px}

/* hero */
.hero{top:112px;height:488px;background:linear-gradient(90deg,#0a1220 0%,#16233a 45%,#3a4a5e 100%)}
.hero .photo{left:560px;top:0;width:640px;height:488px;border-radius:0;background:linear-gradient(135deg,#2c3b50,#7a6a52 55%,#3d4b5d)}
.hero h1{position:absolute;left:72px;top:100px;width:560px;color:#fff;font-size:40px;line-height:1.25;font-weight:600}
.hero .para{position:absolute;left:72px;top:214px;width:440px;color:#cfd6e0}
.hero .btn{position:absolute;left:72px;top:290px}
.dots{position:absolute;left:72px;top:358px;display:flex;gap:8px}
.dots i{display:block;height:4px;width:24px;background:#6b7686;border-radius:2px}
.dots i:first-child{width:44px;background:#fff}

/* about */
.about{top:660px;height:480px}
.feat{position:absolute;display:flex;align-items:center;gap:12px;font-size:14px;font-weight:600;width:210px}
.feat .ico{width:40px;height:40px;border-radius:50%;background:var(--pale);display:flex;align-items:center;justify-content:center;flex:none}

/* band */
.band{top:1212px;height:236px;background:linear-gradient(90deg,var(--blue),#0a63c2);color:#fff;text-align:center}
.band .title{justify-content:center;font-size:44px;margin-top:44px}
.band p{font-size:20px;font-weight:600;margin-top:6px}
.band .btn{background:#fff;color:var(--blue);margin-top:18px}

/* services */
.services{top:1448px;height:432px;background:var(--ink);color:#fff}
.svc-btn{position:absolute;left:72px;width:220px;font-size:13px;font-weight:500;padding:8px 0;text-align:center;border-radius:4px;background:#fff;color:var(--text)}
.svc-btn.active{background:var(--blue);color:#fff}
.card{position:absolute;top:32px;height:280px;border-radius:4px;overflow:hidden}
.card .cap{position:absolute;bottom:18px;left:16px;font-size:14px;font-weight:600;color:#fff}

/* projects */
.projects{top:1912px;height:648px}
.proj-tag{position:absolute;left:16px;bottom:16px;background:#fff;padding:10px 14px;border-radius:2px;width:230px}
.proj-tag b{display:block;color:var(--blue);font-size:15px}
.proj-tag span{font-size:11px;color:var(--muted)}

/* testimonials */
.testi{top:2632px;height:448px;background:var(--blue);color:#fff}
.tcard{position:absolute;top:178px;width:336px;height:176px}
.tcard .pic{left:0;top:0;width:120px;height:176px}
.tcard .box{position:absolute;left:104px;top:14px;width:232px;height:148px;background:#fff;color:var(--text);padding:14px 16px;border-radius:4px}
.tcard h4{font-size:15px;font-weight:600}
.tcard p{font-size:11px;line-height:1.5;color:var(--muted);margin:6px 0}
.stars{color:var(--star);font-size:13px;letter-spacing:2px}

/* stats */
.stats{top:3160px;height:320px}
.stat{position:absolute;top:40px;width:208px;height:248px;border:1px solid #d9dde3;text-align:center}
.stat .ico{width:64px;height:64px;background:var(--pale-2);margin:28px auto 26px;display:flex;align-items:center;justify-content:center}
.stat b{display:block;font-size:40px;font-weight:600}
.stat span{font-size:14px;color:var(--muted)}

/* contact */
.contact{top:3480px;height:440px;background:var(--ink);color:#fff}
.field{position:absolute;height:30px;background:#fff;border-radius:3px;font-size:11px;color:#888;padding:7px 10px}

/* footer */
.footer{top:3920px;height:284px;background:var(--navy);color:#fff}
.footer h5{font-size:16px;font-weight:600;margin-bottom:14px}
.footer li{list-style:none;font-size:13px;color:#c8d1de;margin-bottom:8px;display:flex;align-items:center;gap:8px}
.footer li::before{content:"";width:4px;height:4px;border-radius:50%;background:#c8d1de}
.footer .contact-list li::before{display:none}
.cicon{width:26px;height:26px;border-radius:50%;background:#fff;flex:none;display:flex;align-items:center;justify-content:center}
</style>
</head>
<body>

<header class="section nav">
  <div class="logo"><span class="mark"></span>Pelham &amp; Tracy</div>
  <ul><li>About Us</li><li>Our Services</li><li>Projects</li><li>Testimonials</li><li>Contact Us</li></ul>
  <div class="phone">(555) 014-7654</div>
</header>

<section class="section hero">
  <div class="img photo" role="img" aria-label="Electrician in hard hat working on a switchboard"></div>
  <h1>Reliable Electrical Services for Homes &amp; Businesses</h1>
  <p class="para">Lorem ipsum dolor sit amet, consectetur adipiscing elit, sed do eiusmod tempor incididunt ut labore et dolore magna aliqua.</p>
  <span class="btn">Get a Free Quote</span>
  <div class="dots"><i></i><i></i><i></i></div>
</section>

<section class="section about">
  <div class="img" style="left:72px;top:12px;width:308px;height:376px;background:linear-gradient(160deg,#e9edf2,#b9c3cf 60%,#7b8693)" role="img" aria-label="Company service van parked outside"></div>
  <div class="img" style="left:328px;top:160px;width:224px;height:268px;border:6px solid #fff;background:linear-gradient(170deg,#8aa1b8,#3b4a5e)" role="img" aria-label="Electrician standing beside the van"></div>
  <div class="abs" style="left:680px;top:60px;width:450px">
    <h2 class="title">About Us</h2>
    <p class="para" style="margin-top:12px">Lorem ipsum dolor sit amet, consectetur adipiscing elit, sed do eiusmod tempor incididunt ut labore et dolore magna aliqua. Ut enim ad minim veniam, quis nostrud exercitation ullamco laboris nisi ut aliquip ex ea commodo consequat.</p>
  </div>
  <div class="feat" style="left:680px;top:218px"><span class="ico"><svg width="20" height="20" viewBox="0 0 20 20"><path d="M10 2l2.4 5 5.6.6-4.2 3.8 1.2 5.6L10 14.2 5 17l1.2-5.6L2 7.6 7.6 7z" fill="#0054AA"/></svg></span>10+ Years of Experience</div>
  <div class="feat" style="left:900px;top:218px"><span class="ico"><svg width="20" height="20" viewBox="0 0 20 20"><path d="M10 2l7 3v5c0 4-3 7-7 8-4-1-7-4-7-8V5z" fill="#0054AA"/><path d="M6.5 10l2.5 2.5 4.5-4.5" stroke="#fff" stroke-width="1.8" fill="none"/></svg></span>Licensed &amp; Insured</div>
  <div class="feat" style="left:680px;top:298px"><span class="ico"><svg width="20" height="20" viewBox="0 0 20 20"><circle cx="10" cy="10" r="7.5" stroke="#0054AA" stroke-width="2" fill="none"/><path d="M10 5.5V10l3 2" stroke="#0054AA" stroke-width="2" fill="none"/></svg></span>24/7 Emergency Services</div>
  <div class="feat" style="left:900px;top:298px"><span class="ico"><svg width="20" height="20" viewBox="0 0 20 20"><path d="M3 3h8l6 6-8 8-6-6z" fill="#0054AA"/><circle cx="7" cy="7" r="1.6" fill="#fff"/></svg></span>Transparent Pricing</div>
  <span class="btn abs" style="left:680px;top:384px">Discover More</span>
</section>

<section class="section band on-blue">
  <h2 class="title">Save Energy. Save Money.</h2>
  <p>Energy-efficient electrical upgrades available now!</p>
  <span class="btn">Discover More</span>
</section>

<section class="section services">
  <div class="abs" style="left:72px;top:46px;width:300px">
    <h2 class="title">Our Service</h2>
    <p class="para" style="color:#b8bec8;margin-top:12px">Lorem ipsum dolor sit amet, consectetur adipiscing elit, sed do eiusmod tempor incididunt ut labore et dolore magna aliqua.</p>
  </div>
  <div class="svc-btn active" style="top:172px">Residential Services</div>
  <div class="svc-btn" style="top:220px">Commercial Services</div>
  <div class="svc-btn" style="top:268px">Industrial Services</div>
  <div class="card" style="left:432px;width:228px;background:linear-gradient(160deg,#0a63c2,#0054AA)">
    <div class="abs" style="left:16px;top:80px;width:196px">
      <h4 style="font-size:15px;font-weight:600">Electrical panel</h4>
      <p style="font-size:11px;line-height:1.5;color:#d6e4f5;margin:8px 0">Lorem ipsum dolor sit amet, consectetur adipiscing elit sed do.</p>
      <span style="font-size:12px;font-weight:500">Read more →</span>
    </div>
  </div>
  <div class="card" style="left:676px;width:228px;background:linear-gradient(170deg,#9aa3ad,#3e4650)" role="img" aria-label="Technician repairing a switch"><span class="cap">Switch repair</span></div>
  <div class="card" style="left:920px;width:228px;background:linear-gradient(170deg,#c2b7a4,#4b4a48)" role="img" aria-label="Electrician wiring a panel"><span class="cap">Wiring &amp; rewiring</span></div>
  <div class="card" style="left:1164px;width:36px;background:linear-gradient(170deg,#8a6c3c,#3c3226)" role="img" aria-label="Next service photo"></div>
  <div class="arrows abs" style="left:784px;top:334px">
    <span><svg width="12" height="12" viewBox="0 0 12 12"><path d="M8 2L4 6l4 4" stroke="#0054AA" stroke-width="2" fill="none"/></svg></span>
    <span class="active"><svg width="12" height="12" viewBox="0 0 12 12"><path d="M4 2l4 4-4 4" stroke="#fff" stroke-width="2" fill="none"/></svg></span>
  </div>
</section>

<section class="section projects">
  <div class="abs" style="left:72px;top:36px;width:520px">
    <h2 class="title">Future Projects</h2>
    <p class="para" style="margin-top:12px">Lorem ipsum dolor sit amet, consectetur adipiscing elit, sed do eiusmod tempor incididunt ut labore et dolore magna aliqua.</p>
  </div>
  <div class="arrows abs" style="left:1052px;top:40px">
    <span><svg width="12" height="12" viewBox="0 0 12 12"><path d="M8 2L4 6l4 4" stroke="#0054AA" stroke-width="2" fill="none"/></svg></span>
    <span class="active"><svg width="12" height="12" viewBox="0 0 12 12"><path d="M4 2l4 4-4 4" stroke="#fff" stroke-width="2" fill="none"/></svg></span>
  </div>
  <div class="img" style="left:72px;top:160px;width:356px;height:228px;background:linear-gradient(160deg,#b7bec6,#4d5866)" role="img" aria-label="Team installing a commercial switchboard"></div>
  <div class="img" style="left:436px;top:160px;width:336px;height:228px;background:linear-gradient(160deg,#c9ccd0,#6b7178)" role="img" aria-label="Electrical cabinet with wiring"></div>
  <div class="img" style="left:788px;top:160px;width:340px;height:228px;background:linear-gradient(160deg,#7b7d82,#d5c2a0)" role="img" aria-label="Close-up of hands wiring a panel"></div>
  <div class="img" style="left:72px;top:408px;width:344px;height:232px;background:linear-gradient(160deg,#2a4f9a,#0a2a5c)" role="img" aria-label="Electrician in blue lighting at a control panel">
    <div class="proj-tag"><b>Brightline Electric</b><span>Panel upgrade in the suburbs</span></div>
  </div>
  <div class="img" style="left:432px;top:408px;width:340px;height:232px;background:linear-gradient(160deg,#e6e6e4,#9aa0a6)" role="img" aria-label="Electrician fitting a breaker box"></div>
  <div class="img" style="left:788px;top:408px;width:340px;height:232px;background:linear-gradient(160deg,#d9803a,#5a6068)" role="img" aria-label="Electrician in orange hard hat at a meter board"></div>
</section>

<section class="section testi on-blue">
  <div class="abs" style="left:72px;top:56px;width:700px">
    <h2 class="title">Client Testimonials</h2>
    <p style="font-size:13px;line-height:1.6;color:#d6e4f5;margin-top:10px">Lorem ipsum dolor sit amet, consectetur adipiscing elit, sed do eiusmod tempor incididunt ut labore et dolore magna aliqua.</p>
  </div>
  <div class="arrows abs" style="left:1052px;top:62px">
    <span style="background:#fff"><svg width="12" height="12" viewBox="0 0 12 12"><path d="M8 2L4 6l4 4" stroke="#0054AA" stroke-width="2" fill="none"/></svg></span>
    <span style="background:#cadeef"><svg width="12" height="12" viewBox="0 0 12 12"><path d="M4 2l4 4-4 4" stroke="#0054AA" stroke-width="2" fill="none"/></svg></span>
  </div>
  <div class="tcard" style="left:72px">
    <div class="img pic" style="background:linear-gradient(170deg,#55606e,#1d232b)" role="img" aria-label="Portrait of client Owen R"></div>
    <div class="box"><h4>Owen R</h4><p>Very professional and affordable. They upgraded our entire office system with zero downtime.</p><div class="stars">★★★★★</div></div>
  </div>
  <div class="tcard" style="left:432px">
    <div class="img pic" style="background:linear-gradient(170deg,#c9b8a6,#6d7d92)" role="img" aria-label="Portrait of client Lena M"></div>
    <div class="box"><h4>Lena M</h4><p>Professional, punctual, and reasonably priced. They rewired our whole home and installed new lighting.</p><div class="stars">★★★★★</div></div>
  </div>
  <div class="tcard" style="left:792px">
    <div class="img pic" style="background:linear-gradient(170deg,#d9a58c,#8c5a4c)" role="img" aria-label="Portrait of client Paul S"></div>
    <div class="box"><h4>Paul S</h4><p>We've used them for both our home and our business. Always great service and honest prices.</p><div class="stars">★★★★★</div></div>
  </div>
</section>

<section class="section stats">
  <div class="stat" style="left:72px"><div class="ico"><svg width="32" height="32" viewBox="0 0 32 32"><circle cx="11" cy="11" r="5" fill="#0054AA"/><circle cx="22" cy="11" r="5" fill="#0677BA"/><path d="M2 28c0-6 4-10 9-10s9 4 9 10z" fill="#0054AA"/><path d="M14 28c0-6 3-10 8-10s8 4 8 10z" fill="#0677BA"/></svg></div><b>10K+</b><span>Satisfied Clients</span></div>
  <div class="stat" style="left:352px"><div class="ico"><svg width="32" height="32" viewBox="0 0 32 32"><path d="M9 4h14v8a7 7 0 01-14 0z" fill="#0054AA"/><path d="M14 19h4v5h-4z" fill="#0054AA"/><path d="M9 26h14v3H9z" fill="#0677BA"/></svg></div><b>2K+</b><span>Awards Wining</span></div>
  <div class="stat" style="left:640px"><div class="ico"><svg width="32" height="32" viewBox="0 0 32 32"><path d="M5 28V18h5v10zM13.5 28V12h5v16zM22 28V6h5v22z" fill="#0054AA"/></svg></div><b>12K+</b><span>Project Complete</span></div>
  <div class="stat" style="left:920px"><div class="ico"><svg width="32" height="32" viewBox="0 0 32 32"><path d="M16 3l11 4v8c0 7-5 12-11 14C10 27 5 22 5 15V7z" fill="#0054AA"/><path d="M11 16l4 4 7-7" stroke="#fff" stroke-width="2.5" fill="none"/></svg></div><b>100%</b><span>Guarantee</span></div>
</section>

<section class="section contact">
  <div class="img" style="left:0;top:0;width:600px;height:440px;border-radius:0;background:linear-gradient(180deg,#8a7a66 0%,#5d6470 45%,#2c333d 100%)" role="img" aria-label="Company team standing in front of service vans"></div>
  <div class="abs" style="left:680px;top:44px;width:440px;text-align:center">
    <h2 class="title light" style="justify-content:center">Contact Us</h2>
    <p style="font-size:14px;font-weight:500;margin-top:4px">Need Electrical Help? Let's Talk!</p>
  </div>
  <div class="field" style="left:680px;top:130px;width:432px">Enter Your Name</div>
  <div class="field" style="left:680px;top:172px;width:212px">Enter Your Phone Number</div>
  <div class="field" style="left:900px;top:172px;width:212px">Email Address</div>
  <div class="field" style="left:680px;top:214px;width:212px">Select Your Service ▾</div>
  <div class="field" style="left:900px;top:214px;width:212px">Enter Your Location</div>
  <div class="field" style="left:680px;top:256px;width:432px;height:88px">Message</div>
  <div class="abs" style="left:680px;top:356px;width:432px;background:var(--blue);color:#fff;text-align:center;font-size:13px;font-weight:500;padding:8px 0;border-radius:16px">Submit</div>
</section>

<footer class="section footer">
  <div class="abs" style="left:72px;top:44px;width:300px">
    <div class="logo" style="color:#fff"><span class="mark" style="background:#fff"></span>Pelham &amp; Tracy</div>
    <p style="font-size:13px;line-height:1.6;color:#c8d1de;margin-top:14px">Lorem ipsum dolor sit amet, consectetur adipiscing elit, sed do eiusmod tempor.</p>
    <div style="display:flex;gap:10px;margin-top:16px"><span class="cicon"></span><span class="cicon"></span><span class="cicon"></span></div>
  </div>
  <div class="abs" style="left:440px;top:44px"><h5>Quick Links</h5><ul><li>Home</li><li>About Us</li><li>Projects</li><li>Testimonials</li></ul></div>
  <div class="abs" style="left:680px;top:44px"><h5>Our Services</h5><ul><li>Residential</li><li>Commercial</li><li>Industrial</li></ul></div>
  <div class="abs" style="left:930px;top:44px;width:200px"><h5>Contact Us</h5>
    <ul class="contact-list">
      <li><span class="cicon"><svg width="12" height="12" viewBox="0 0 12 12"><path d="M3 1l2 3-1 1c.7 1.4 1.6 2.3 3 3l1-1 3 2-1 2C5 11 1 7 1 2z" fill="#071a36"/></svg></span>(555) 014-7654</li>
      <li><span class="cicon"><svg width="12" height="12" viewBox="0 0 12 12"><path d="M6 1a3.5 3.5 0 013.5 3.5C9.5 7 6 11 6 11S2.5 7 2.5 4.5A3.5 3.5 0 016 1z" fill="#071a36"/><circle cx="6" cy="4.5" r="1.2" fill="#fff"/></svg></span><span style="font-size:12px;line-height:1.4">128 Alder Lane,<br>Brookfield NH 03000</span></li>
      <li><span class="cicon"><svg width="12" height="12" viewBox="0 0 12 12"><rect x="1" y="2.5" width="10" height="7" fill="#071a36"/><path d="M1 3l5 3.5L11 3" stroke="#fff" fill="none"/></svg></span>info@pelham-tracy.com</li>
    </ul>
  </div>
  <div class="abs" style="left:72px;top:236px;width:1056px;border-top:1px solid #24395a;padding-top:12px;display:flex;justify-content:space-between;font-size:12px;color:#c8d1de">
    <span>© 2024 All rights Reserved</span><span>Privacy Policy &nbsp;|&nbsp; Term &amp; Conditions</span>
  </div>
</footer>

</body>
</html>
```